Velvet Bloom Marisol's Cleaning Service Business Cards Project

A business card with all contact details with logo design on there (already have a logo) eye catching Logo and contact info on one side, full logo on the back, must target upper class residential and corporate companies, fitness companies, still keep it on the feminine side of things , must look elegant

Target Market(s)

Upper class homes and corporate companies

Industry/Entity Type

Cleaning Service

Contact Information for Business Card

Name: Marisol Denhart
Position: Director
ABN: 47193062857
Email: marisolsvelvetcleaning@brightmail.example
Number: 0418926547

Font styles to use
Decorative

Colors

Designer to choose colors to be used in the design.

Requirements
Must have
• Available Sydney Wide, contact info and logo on one side, full logo on the back
Nice to have
• Professional appearance
Should not have
• Cheap advert looking stuff

```html
<!DOCTYPE html>
<html lang="en">
<head>
<meta charset="utf-8">
<title>Velvet Bloom – Business Cards</title>
<link rel="stylesheet" href="https://fonts.googleapis.com/css2?family=Cinzel:wght@400;600&family=Lato:wght@400;700&display=swap">
<style>
  :root {
    --teal: #2fe3d9;
    --teal-deep: #22cfc5;
    --aqua-light: #8ff6f0;
    --navy: #30343f;
    --ink: #22252c;
    --paper: #ffffff;
    --backdrop: #3a3d44;
  }
  * { box-sizing: border-box; margin: 0; padding: 0; }
  html, body {
    width: 1200px; height: 782px; overflow: hidden;
    background: var(--backdrop);
  }
  .stage {
    width: 1200px; height: 782px;
    display: flex; align-items: center; justify-content: center; gap: 40px;
  }
  .card {
    position: relative;
    width: 540px; height: 300px;
    overflow: hidden;
    box-shadow: 0 10px 28px rgba(0,0,0,.45);
  }

  /* Front */
  .card-front { background: var(--paper); color: var(--ink); font-family: "Lato", sans-serif; }
  .holder-name {
    position: absolute; left: 34px; top: 30px;
    font-family: "Cinzel", serif; font-weight: 400;
    font-size: 21px; letter-spacing: 1px; color: var(--teal-deep);
  }
  .holder-role { position: absolute; left: 34px; top: 58px; font-size: 12px; color: var(--ink); }
  .contact-list { position: absolute; left: 34px; top: 94px; list-style: none; font-size: 13.5px; }
  .contact-list li { display: flex; align-items: center; gap: 8px; line-height: 22px; white-space: nowrap; }
  .contact-list .abn { margin-bottom: 10px; }
  .label { color: var(--teal-deep); }
  .icon { width: 12px; height: 12px; fill: var(--teal-deep); flex: none; }
  .brand-mark {
    position: absolute; right: 30px; top: 100px;
    display: flex; align-items: center; gap: 10px;
    font-family: "Cinzel", serif; font-weight: 600;
    font-size: 22px; letter-spacing: 1.5px; color: var(--teal-deep);
    white-space: nowrap;
  }
  .brand-dot { width: 14px; height: 14px; border-radius: 50%; background: var(--teal-deep); flex: none; }
  .waves { position: absolute; left: 0; bottom: 0; width: 540px; height: 300px; }

  /* Back */
  .card-back { background: var(--teal); }
  .pattern-field { position: absolute; inset: 0; background: var(--teal); }
  .back-name {
    position: absolute; inset: 0;
    display: flex; align-items: center; justify-content: center;
    font-family: "Cinzel", serif; font-weight: 600;
    font-size: 26px; letter-spacing: 2px; color: var(--paper);
  }
</style>
</head>
<body>
<main class="stage">
  <section class="card card-front" aria-label="Business card front">
    <svg class="waves" viewBox="0 0 540 300" aria-hidden="true">
      <path d="M0,186 C90,222 200,242 330,252 C420,259 490,268 540,290 L540,300 L0,300Z" fill="var(--aqua-light)"/>
      <path d="M330,260 C430,263 500,275 540,292 L540,300 L300,300Z" fill="var(--teal)"/>
      <path d="M0,206 C70,248 180,264 300,269 C400,274 470,281 520,300 L0,300Z" fill="var(--paper)"/>
      <path d="M0,212 C70,254 180,270 300,275 C390,280 455,288 495,300 L0,300Z" fill="var(--navy)"/>
    </svg>

    <h1 class="holder-name">Marisol Denhart</h1>
    <p class="holder-role">Director</p>

    <ul class="contact-list">
      <li class="abn"><span class="label">ABN:</span> 47193062857</li>
      <li>
        <svg class="icon" viewBox="0 0 24 24" aria-hidden="true"><path d="M6.6 10.8a15.1 15.1 0 0 0 6.6 6.6l2.2-2.2a1 1 0 0 1 1-.25 11.4 11.4 0 0 0 3.6.57 1 1 0 0 1 1 1V20a1 1 0 0 1-1 1A17 17 0 0 1 3 4a1 1 0 0 1 1-1h3.5a1 1 0 0 1 1 1c0 1.25.2 2.45.57 3.57a1 1 0 0 1-.25 1z"/></svg>
        0418926547
      </li>
      <li>
        <svg class="icon" viewBox="0 0 24 24" aria-hidden="true"><path d="M2 5h20v14H2z" fill="var(--teal-deep)"/><path d="M3.5 6.5 12 13l8.5-6.5" fill="none" stroke="#fff" stroke-width="1.6"/></svg>
        marisolsvelvetcleaning@brightmail.example
      </li>
    </ul>

    <div class="brand-mark">
      <span class="brand-dot" aria-hidden="true"></span>
      <span>Velvet Bloom</span>
    </div>
  </section>

  <section class="card card-back" aria-label="Business card back">
    <div class="pattern-field" role="img" aria-label="Repeating pattern of the brand symbol in pale teal outlines"></div>
    <p class="back-name">Velvet Bloom</p>
  </section>
</main>
</body>
</html>
```